NEW Modern Sleek Business Card for VR Language Startup

Our startup is using VR to lead the next wave of world language education. We need a two-sided business card that introduces the larger organization (Brightvale Tongues Inc) and our contact info on one side and shows the product, Lexiquorra, on the other side.

Side 1 (contact info)= Brightvale Logo and Contact info (name, title, phone, email)

Side 2 (product)= Lexiquora logo, text, and website
Text= Culturally Immersive Language Learning Games
Website= www.lexiquora-demo.test

Target Market(s)

Education, Technology

Contact Information for Business Card

Contact info will be updated upon approval of the design. For now, put this as a placeholder.

Peter Hallow
Founder & CEO
phallow@mailbox-demo.test
(555)-010-4477

Font styles to use
Other font styles liked:
• Gibson and Century Gothic are the brand fonts

Requirements
Nice to have
• I would love to see cohesion between the design and colors of the two logos. I have attached a few business card designs that I like, so you can get a feel for my preferred style.

```html
<!DOCTYPE html>
<html lang="en">
<head>
<meta charset="utf-8">
<title>Brightvale Tongues Inc — Business Card</title>
<link href="https://fonts.googleapis.com/css2?family=Questrial&family=Montserrat:wght@400;600;700&display=swap" rel="stylesheet">
<style>
  :root {
    --page-bg: #e8ebee;
    --card-white: #ffffff;
    --ink-grey: #55585c;
    --ink-dark: #1d1d1f;
    --accent-blue: #2f7fd8;
    --icon-blue: #3a6fd0;
    --warm-orange: #f7a21b;
    --warm-red: #ee3a4a;
    --mid-purple: #8b3fb8;
    --cool-cyan: #2cc3ee;
    --back-deep: #4a4aa6;
    --back-mid: #4f6fbc;
    --back-light: #58a6d2;
    --back-text: #ffffff;
  }
  * { box-sizing: border-box; margin: 0; padding: 0; }
  html, body {
    width: 1200px; height: 900px; overflow: hidden;
    background: var(--page-bg);
  }
  .canvas {
    width: 1200px; height: 900px;
    display: flex; flex-direction: column; align-items: center; justify-content: center;
    gap: 60px;
  }
  .card {
    width: 640px; height: 366px; position: relative; overflow: hidden;
    box-shadow: 0 6px 18px rgba(0,0,0,0.12);
  }

  /* Side 1 — contact */
  .card--contact { background: var(--card-white); font-family: "Montserrat", "Questrial", sans-serif; }
  .company-mark {
    position: absolute; left: 44px; top: 62px;
    display: flex; align-items: center; gap: 12px;
  }
  .company-mark__dot {
    width: 38px; height: 38px; border-radius: 50%;
    background: linear-gradient(135deg, var(--warm-orange), var(--warm-red) 45%, var(--mid-purple) 75%, var(--cool-cyan));
  }
  .company-mark__name {
    font-weight: 700; font-size: 24px; letter-spacing: 4px; color: var(--ink-dark);
    text-transform: uppercase;
  }
  .brand-art {
    position: absolute; right: 34px; top: 40px; width: 220px; height: 286px; border-radius: 110px;
    background: linear-gradient(160deg, var(--warm-orange) 0%, var(--warm-red) 35%, var(--mid-purple) 65%, var(--cool-cyan) 100%);
    opacity: 0.9;
  }
  .contact {
    position: absolute; left: 88px; top: 180px;
  }
  .contact__name { font-family: "Questrial", sans-serif; font-size: 21px; color: var(--ink-grey); }
  .contact__title { font-family: "Questrial", sans-serif; font-size: 15px; color: var(--accent-blue); margin-top: 2px; }
  .contact__list { list-style: none; margin-top: 26px; }
  .contact__item {
    display: flex; align-items: center; gap: 10px;
    font-family: "Questrial", sans-serif; font-size: 15px; color: var(--ink-grey);
    margin-bottom: 9px;
  }
  .contact__icon {
    width: 20px; height: 20px; border-radius: 50%; background: var(--icon-blue);
    display: flex; align-items: center; justify-content: center;
  }

  /* Side 2 — product */
  .card--product {
    background: linear-gradient(215deg, var(--back-deep) 0%, var(--back-mid) 50%, var(--back-light) 100%);
    color: var(--back-text); font-family: "Questrial", sans-serif;
  }
  .product-art {
    position: absolute; left: -60px; top: 40px; width: 330px; height: 340px; border-radius: 50%;
    background: radial-gradient(circle at 60% 45%, rgba(120,200,230,0.45), rgba(90,150,210,0.15) 70%, transparent);
  }
  .product {
    position: absolute; left: 250px; top: 96px; width: 350px; text-align: center;
  }
  .product__mark { display: flex; align-items: center; justify-content: center; gap: 12px; }
  .product__dot { width: 30px; height: 30px; border-radius: 50%; background: var(--back-text); }
  .product__name { font-family: "Montserrat", sans-serif; font-weight: 700; font-size: 44px; }
  .product__tagline { font-size: 15px; margin-top: 18px; letter-spacing: 0.3px; }
  .product__web {
    display: flex; align-items: center; gap: 12px; justify-content: center;
    font-size: 13px; margin-top: 8px; letter-spacing: 0.5px;
  }
  .rule { display: block; height: 1px; width: 60px; background: rgba(255,255,255,0.8); }
  .product__frame-line {
    position: absolute; height: 1px; background: rgba(255,255,255,0.7); width: 180px;
  }
  .product__frame-line--top { right: 30px; top: 60px; }
  .product__frame-line--bottom { left: 260px; bottom: 50px; }
</style>
</head>
<body>
<main class="canvas">
  <section class="card card--contact" aria-label="Contact side">
    <div class="company-mark">
      <span class="company-mark__dot"></span>
      <span class="company-mark__name">Brightvale</span>
    </div>
    <div class="brand-art" role="img" aria-label="Large brand mark area in warm-to-cool gradient"></div>
    <div class="contact">
      <p class="contact__name">Peter HALLOW</p>
      <p class="contact__title">Founder | CEO</p>
      <ul class="contact__list">
        <li class="contact__item">
          <span class="contact__icon">
            <svg width="11" height="11" viewBox="0 0 24 24"><path fill="#fff" d="M6.6 10.8a15 15 0 0 0 6.6 6.6l2.2-2.2c.3-.3.7-.4 1-.2 1.1.4 2.3.6 3.6.6.6 0 1 .4 1 1V20c0 .6-.4 1-1 1A17 17 0 0 1 3 4c0-.6.4-1 1-1h3.5c.6 0 1 .4 1 1 0 1.3.2 2.5.6 3.6.1.3 0 .7-.2 1z"/></svg>
          </span>
          (555)-010-4477
        </li>
        <li class="contact__item">
          <span class="contact__icon">
            <svg width="11" height="11" viewBox="0 0 24 24"><path fill="#fff" d="M3 5h18v14H3z"/><path fill="none" stroke="#3a6fd0" stroke-width="2" d="M3 6l9 7 9-7"/></svg>
          </span>
          phallow@mailbox-demo.test
        </li>
      </ul>
    </div>
  </section>

  <section class="card card--product" aria-label="Product side">
    <div class="product-art" role="img" aria-label="Soft circuit-style product illustration area"></div>
    <span class="product__frame-line product__frame-line--top"></span>
    <div class="product">
      <div class="product__mark">
        <span class="product__dot"></span>
        <span class="product__name">Lexiquora</span>
      </div>
      <p class="product__tagline">Culturally Immersive Language Learning Games</p>
      <p class="product__web"><span class="rule"></span>www.lexiquora-demo.test<span class="rule"></span></p>
    </div>
    <span class="product__frame-line product__frame-line--bottom"></span>
  </section>
</main>
</body>
</html>
```